Democracy in crisis book

This book tries to sound the ALARM that we will lose our democracy unless we force Unionists to adopt the plan inside this book. I designed a mock cover (attached) but I am concerned it would not look good in the Thumbnail view that most people would see it as they're scrolling down Shopvale or Pagenook. The final title for the book is: Final Hour to Rescue the Free Republic. The current subtitle is: The Single Path to Halt the 2022 Partisan Takeover & Renew Our Homeland -- but it’s a work in progress.The subtitle is still working progress but it's really not that important and can be small.
STYLE CONSIDERATIONS:
(1) The title should be on 5 separate lines: Final; Hour; To Rescue; Free; Republic
(2) The title could be in white fat letters except for maybe one line that says “To Rescue” which could be in the blue color of the Civic Union Party-- or maybe Free Republic could be in blue. We may have to try a few variations of that.
(3) I picked the red in the mock cover to connotate an emergency,
(4) I liked big bold fat font going across the full page so that it looks like a major warning sign, though note I was unable to extend each line flush all the way to the right which I think would have been better.
(5) I liked it better flush to left instead of centered.
(6) I picked the Harwick monument + a crowd for my mock cover, but a picture of a huge crowd protesting with a picture of the United States Congress in the background would be much better. DO NOT USE HARWICK. Obviously I would need it to be an open license or something I can pay a small amount to get. If you can find that picture then the page should probably be colored in red with Congress in white.
I got the idea 4 giant title from the book “seldom a quiet so bright” and Dellowby’s “When Freedom Fades” or “Grey Herons” by Mara Vostell though I hate that font)
I love Osric Thale’s “marked since the outset” cover so if you find a picture of Congress and a protest crowd instead of painting it red you could have just a couple of jagged red stripes going across it like that cover.
I love the 3-D effect of Greta Wolven's cover for The Silverwren where it looks like a page is being ripped. That effect could be done the words Free Republic like it's being torn off the page UPDATE: MANY DESIGNERS TRIED THAT & IT DID NOT WORK AT ALL.
Note that this book will be submitted to many award competitions, so please give me an award-winning cover.
I like how the title of the book The Unchosen by Martin Fellowes has the words starting to fade. I don't like the ladder on it, but maybe 'Free Republic' could fade like that.
Unionists

```html
<!DOCTYPE html>
<html lang="en">
<head>
<meta charset="utf-8">
<title>Final Hour to Rescue the Free Republic — Cover</title>
<link href="https://fonts.googleapis.com/css2?family=Archivo+Black&display=swap" rel="stylesheet">
<style>
  :root {
    --page: #ffffff;
    --navy: #22336b;
    --navy-deep: #18244f;
    --navy-soft: #34477f;
    --title-white: #eceef3;
    --union-blue: #4db3e8;
    --strip-white: #fdfdfb;
    --strip-edge: #d6d0c2;
    --subtitle: #c9cede;
  }
  * { margin: 0; padding: 0; box-sizing: border-box; }
  html, body {
    width: 1200px;
    height: 848px;
    overflow: hidden;
    background: var(--page);
  }
  .canvas {
    position: relative;
    width: 1200px;
    height: 848px;
    background: var(--page);
  }
  .book-cover {
    position: absolute;
    left: 348px;
    top: 40px;
    width: 504px;
    height: 768px;
    overflow: hidden;
    background: var(--navy);
    font-family: "Archivo Black", "Arial Black", sans-serif;
  }
  .cover-scene {
    position: absolute;
    inset: 0;
    background:
      radial-gradient(ellipse 55% 30% at 45% 22%, rgba(120, 135, 180, 0.35), transparent 70%),
      linear-gradient(178deg, transparent 56%, rgba(20, 28, 60, 0.55) 60%, transparent 64%),
      linear-gradient(176deg, transparent 68%, rgba(16, 22, 50, 0.6) 72%, transparent 80%),
      linear-gradient(180deg, var(--navy-soft) 0%, var(--navy) 40%, var(--navy-deep) 75%, var(--navy) 100%);
  }
  .title-line {
    position: absolute;
    left: 24px;
    color: var(--title-white);
    line-height: 1;
    white-space: nowrap;
    text-transform: uppercase;
  }
  .title-final   { top: 88px;  font-size: 106px; letter-spacing: 2px; }
  .title-hour    { top: 172px; font-size: 106px; letter-spacing: 4px; }
  .title-free    { top: 392px; font-size: 78px;  letter-spacing: 6px; }
  .title-republic{ top: 474px; font-size: 64px;  letter-spacing: 2px; }
  .torn-strip {
    position: absolute;
    left: 0;
    top: 256px;
    width: 504px;
    height: 112px;
  }
  .title-rescue {
    position: absolute;
    left: 44px;
    top: 284px;
    font-size: 60px;
    letter-spacing: 1px;
    color: var(--union-blue);
    line-height: 1;
    white-space: nowrap;
    text-transform: uppercase;
  }
  .subtitle {
    position: absolute;
    left: 30px;
    top: 566px;
    width: 380px;
    font-size: 15px;
    line-height: 1.2;
    letter-spacing: 1.2px;
    color: var(--subtitle);
  }
</style>
</head>
<body>
  <main class="canvas">
    <section class="book-cover">
      <div class="cover-scene" role="img" aria-label="Faded photograph of the United States Capitol above a protest crowd, overlaid with a navy-tinted flag and dark brush strokes"></div>

      <h1 class="book-title">
        <span class="title-line title-final">Final</span>
        <span class="title-line title-hour">Hour</span>
        <svg class="torn-strip" viewBox="0 0 504 112" aria-hidden="true">
          <polygon fill="var(--strip-edge)"
            points="4,14 40,9 90,11 140,7 200,9 260,6 320,8 380,5 440,7 504,4 504,112 460,110 400,111 340,108 280,110 220,107 160,109 100,106 44,108 38,90 30,60 20,36"/>
          <polygon fill="#ecebe4"
            points="6,18 26,16 36,34 30,22"/>
          <polygon fill="var(--strip-white)"
            points="22,17 70,15 120,16 180,13 240,15 300,12 360,14 420,11 480,13 504,11 504,104 450,103 390,105 330,102 270,104 210,101 150,103 94,100 50,102 44,82 36,52 28,30"/>
        </svg>
        <span class="title-rescue">To Rescue</span>
        <span class="title-line title-free">Free</span>
        <span class="title-line title-republic">Republic</span>
      </h1>

      <p class="subtitle">The Single Path to Halt the 2022 Partisan Takeover &amp; Renew Our Homeland</p>
    </section>
  </main>
</body>
</html>
```